Mirela Dawn Business Card Design

I need a business card for my daughter. She has it all described in the file below. But it needs to be square in shape. http://www.mireladawn.example is her web site

Target Market(s)

18-35 year old women

Industry/Entity Type

Fashion

Contact Information for Business Card

Please look at the attached file as it has all the details.

Requirements
Must have
• Please look at the attached file as it has all the details.
Nice to have
Should not have

```html
<!DOCTYPE html>
<html lang="en">
<head>
<meta charset="utf-8">
<title>Mirela Dawn – Square Business Card</title>
<link rel="stylesheet" href="https://fonts.googleapis.com/css2?family=Abril+Fatface&family=Caveat:wght@500&family=Roboto:wght@500&display=swap">
<style>
  :root {
    --blush: #f7c4dc;
    --ink: #000000;
    --paper: #ffffff;
    --olive: #5b5636;
    --olive-deep: #2a2818;
    --display: "Abril Fatface", "Times New Roman", serif;
    --script: "Caveat", "Comic Sans MS", cursive;
    --body: "Roboto", Arial, sans-serif;
  }
  * { margin: 0; padding: 0; box-sizing: border-box; }
  html, body { width: 1200px; height: 1000px; overflow: hidden; background: var(--paper); }
  .canvas { position: relative; width: 1200px; height: 1000px; }

  .card {
    position: absolute; top: 256px; width: 490px; height: 489px;
    background: var(--blush);
    box-shadow: 1px 2px 3px rgba(0,0,0,0.25);
  }
  .card--front { left: 70px; }
  .card--back { left: 615px; }
  .card__face {
    position: absolute; left: 13px; top: 13px; right: 14px; bottom: 14px;
    background: var(--ink); overflow: hidden;
  }

  .texture {
    position: absolute; inset: 0;
    background:
      radial-gradient(ellipse at 20% 85%, rgba(91,86,54,0.75), transparent 55%),
      radial-gradient(ellipse at 80% 20%, rgba(91,86,54,0.55), transparent 50%),
      linear-gradient(160deg, var(--olive-deep), #0d0c07 55%, var(--olive-deep));
  }
  .front__name {
    position: absolute; left: 0; right: 0; top: 176px;
    text-align: center; font-family: var(--display); color: var(--blush);
    font-size: 46px; letter-spacing: 2px; line-height: 1;
  }
  .front__rule {
    position: absolute; left: 109px; width: 244px; top: 229px;
    height: 2px; background: var(--paper);
  }
  .front__tagline {
    position: absolute; left: 0; right: 0; top: 240px;
    text-align: center; font-family: var(--script); color: var(--blush);
    font-size: 32px; line-height: 1;
  }

  .back__band {
    position: absolute; left: 23px; top: 21px; width: 418px; height: 38px;
    background: var(--blush); color: var(--ink);
    font-family: var(--script); font-size: 25px; line-height: 38px;
    text-align: center; white-space: nowrap;
  }
  .back__name {
    position: absolute; left: 44px; top: 120px;
    font-family: var(--display); color: var(--blush);
    font-size: 31px; letter-spacing: 1.5px; line-height: 1;
  }
  .contacts { position: absolute; left: 49px; top: 218px; list-style: none; }
  .contacts__item {
    display: flex; align-items: center; height: 26px;
    font-family: var(--body); color: var(--paper); font-size: 16px;
  }
  .contacts__icon {
    width: 18px; height: 18px; border-radius: 50%; background: var(--blush);
    margin-right: 17px; flex: none;
  }
  .contacts__icon svg { display: block; }
  .links { position: absolute; left: 49px; top: 356px; }
  .links__row {
    height: 27px; font-family: var(--body); color: var(--paper); font-size: 16px;
  }
  .links__label {
    font-family: var(--display); color: var(--blush); font-size: 16px; letter-spacing: 1px;
  }
</style>
</head>
<body>
<div class="canvas">

  <section class="card card--front">
    <div class="card__face">
      <div class="texture" role="img" aria-label="Olive-gold paint scratch texture over black"></div>
      <h1 class="front__name">MIRELA DAWN</h1>
      <div class="front__rule"></div>
      <p class="front__tagline">let's talk fashion</p>
    </div>
  </section>

  <section class="card card--back">
    <div class="card__face">
      <p class="back__band">blogger &amp; vlogger//beauty-fashion-travel</p>
      <h2 class="back__name">MIRELA DAWN</h2>
      <ul class="contacts">
        <li class="contacts__item"><span class="contacts__icon"></span>photogram.example/mireladawnxo</li>
        <li class="contacts__item"><span class="contacts__icon"></span>chirper.example/mireladawnxo</li>
        <li class="contacts__item"><span class="contacts__icon"></span>@mireladawnxo</li>
        <li class="contacts__item"><span class="contacts__icon">
          <svg width="18" height="18" viewBox="0 0 18 18"><rect x="4.5" y="5.5" width="9" height="7" fill="none" stroke="#000" stroke-width="1.3"/><path d="M4.5 5.5 L9 9.5 L13.5 5.5" fill="none" stroke="#000" stroke-width="1.3"/></svg>
        </span>mirela@mireladawn.example</li>
      </ul>
      <div class="links">
        <p class="links__row"><span class="links__label">BLOG:</span> mireladawn.example</p>
        <p class="links__row"><span class="links__label">VIDTUBE:</span> vidtube.example/mireladawn</p>
      </div>
    </div>
  </section>

</div>
</body>
</html>
```